Locksmith Business Cards

My father-in-law is in need of new business cards for his locksmith business and I need to impress him. Kindly help me out!

You can see the previous business card attached. It is a family run business in North Wales.

No individual names on the cards.

Key Things to Feature:
- The words "Prompt", "Local", "Reliable" (as you can see under the logo on the website)
- 24h Emergency Service
- Covering All of North Wales, the Wirral and Chester
- The color blue
- A key or a lock would be interesting (similar to the ones that come up when you google locksmith business card)

Optional (only if design includes bullet points, like the example below):
https://imgvaultcdnx.net/design_img/318264/57190/57190_2749031_318264_image.jpg
- Residential / Commercial / Automotive
- Alarms & Cameras
- Key Cutting & Safes

https://www.bryncoed-locksmiths-demo.co.uk/

Locksmith

01632 960 418
07700 900 362
bryncoedlocksmiths@mailvalex.com
Bryncoed Locksmiths, Hafod Barn, 4 Pennant Rd., Llandudno LL39 7QZ
www.bryncoed-locksmiths-demo.co.uk

• - The words "Prompt", "Local", "Reliable" (as you can see under the logo on the website)
• - 24h Emergency Service
• - Covering All of North Wales, the Wirral and Chester
• - A key or a lock would be interesting (similar to the ones that come up when you google locksmith business card)

```html
<!DOCTYPE html>
<html lang="en">
<head>
<meta charset="utf-8">
<title>Bryncoed Locksmiths – Business Cards</title>
<link rel="stylesheet" href="https://fonts.googleapis.com/css2?family=Open+Sans:wght@400;600;700&display=swap">
<style>
  :root {
    --backdrop: #141415;
    --card: #212123;
    --card-edge: #2c2c2f;
    --silver: #cfd0d2;
    --silver-dim: #9a9b9e;
    --text: #e4e4e6;
    --rule: #4a4a4e;
    --blue: #2f3f8f;
    --blue-light: #4658b0;
  }
  * { box-sizing: border-box; margin: 0; padding: 0; }
  html, body {
    width: 1200px; height: 900px; overflow: hidden;
    background: var(--backdrop);
    font-family: "Open Sans", Arial, sans-serif;
    color: var(--text);
  }
  .stage {
    width: 1200px; height: 900px;
    display: flex; flex-direction: column; align-items: center; justify-content: center;
    gap: 50px;
  }
  .card {
    position: relative;
    width: 600px; height: 343px;
    background: var(--card);
    border: 1px solid var(--card-edge);
    border-radius: 22px;
    box-shadow: 0 14px 30px rgba(0,0,0,.55);
  }

  /* Front */
  .front .brand {
    position: absolute; top: 92px; right: 60px; width: 340px;
    text-align: center;
  }
  .brand-name {
    display: flex; align-items: center; justify-content: center; gap: 12px;
    font-weight: 600; font-size: 30px; letter-spacing: 1px; line-height: 1.1;
    text-transform: uppercase;
  }
  .brand-name .mark { width: 16px; height: 16px; border-radius: 50%; flex: none; }
  .front .brand-name { color: var(--silver); }
  .front .brand-name .mark { background: var(--silver); }
  .tagline {
    margin-top: 10px;
    font-size: 13px; font-weight: 600; letter-spacing: 2px;
    color: var(--silver-dim);
  }
  .front .rule {
    position: absolute; left: 220px; right: 50px; top: 222px;
    border-top: 1px solid var(--rule);
  }
  .services {
    position: absolute; left: 220px; right: 50px; top: 238px;
    text-align: center; font-size: 15px; line-height: 1.45;
  }
  .services .dot {
    display: inline-block; width: 6px; height: 6px; border-radius: 50%;
    background: var(--text); vertical-align: middle; margin: 0 8px 3px;
  }

  /* Back */
  .back .brand-name {
    position: absolute; top: 40px; right: 48px;
    color: var(--blue-light); font-size: 28px;
  }
  .back .brand-name .mark { background: var(--blue); width: 14px; height: 14px; }
  .address {
    position: absolute; top: 100px; right: 50px;
    text-align: right; font-size: 15px; line-height: 1.5;
  }
  .back .rule-top {
    position: absolute; top: 130px; right: 50px; width: 230px; display: none;
  }
  .contacts {
    position: absolute; left: 40px; top: 178px;
    list-style: none; font-size: 16px; line-height: 1.45;
  }
  .contacts li { display: flex; align-items: center; gap: 9px; }
  .contacts svg { width: 15px; height: 15px; flex: none; fill: var(--blue-light); }
  .back .rule {
    position: absolute; left: 40px; right: 50px; top: 278px;
    border-top: 1px solid var(--rule);
  }
  .coverage {
    position: absolute; left: 40px; right: 50px; top: 284px;
    text-align: center; font-size: 15px; line-height: 1.35;
  }
  .coverage .emergency { font-weight: 700; letter-spacing: .3px; }
  .coverage a { color: inherit; text-decoration: none; }
</style>
</head>
<body>
<main class="stage">

  <section class="card front" aria-label="Card front">
    <div class="brand">
      <div class="brand-name"><span class="mark"></span>Bryncoed Locksmiths</div>
      <p class="tagline">PROMPT. LOCAL. RELIABLE</p>
    </div>
    <div class="rule"></div>
    <p class="services">
      Residential / Commercial / Automotive<br>
      Alarms &amp; Cameras<span class="dot"></span>Key Cutting &amp; Safes
    </p>
  </section>

  <section class="card back" aria-label="Card back">
    <div class="brand-name"><span class="mark"></span>Bryncoed Locksmiths</div>
    <address class="address" style="font-style:normal">
      Bryncoed Locksmiths<br>
      Hafod Barn<br>
      4 Pennant Rd.,<br>
      Llandudno LL39 7QZ
    </address>
    <ul class="contacts">
      <li><svg viewBox="0 0 16 16" aria-hidden="true"><path d="M3 2h3l1 3-2 1.5a9 9 0 0 0 4.5 4.5L11 9l3 1v3a1 1 0 0 1-1 1A12 12 0 0 1 2 3a1 1 0 0 1 1-1z"/></svg>01632 960 418</li>
      <li><svg viewBox="0 0 16 16" aria-hidden="true"><path d="M5 1h6a1 1 0 0 1 1 1v12a1 1 0 0 1-1 1H5a1 1 0 0 1-1-1V2a1 1 0 0 1 1-1zm0 2v9h6V3zm3 10a.8.8 0 1 0 0 .01z"/></svg>07700 900 362</li>
      <li><svg viewBox="0 0 16 16" aria-hidden="true"><path d="M1 3h14v10H1zm1.5 1.2V5l5.5 4 5.5-4v-.8L8 8z"/></svg>bryncoedlocksmiths@mailvalex.com</li>
      <li><svg viewBox="0 0 16 16" aria-hidden="true"><path d="M8 1a7 7 0 1 0 0 14A7 7 0 0 0 8 1zm-1 2.2V6H4.2A5 5 0 0 1 7 3.2zM9 3.2A5 5 0 0 1 11.8 6H9zM3.1 8H7v4.8A5 5 0 0 1 3.1 8zM9 12.8V8h3.9A5 5 0 0 1 9 12.8z"/></svg>www.bryncoed-locksmiths-demo.co.uk</li>
    </ul>
    <div class="rule"></div>
    <p class="coverage">
      <span class="emergency">24H EMERGENCY SERVICE</span><br>
      Covering All of North Wales, the Wirral and Chester
    </p>
  </section>

</main>
</body>
</html>
```